Business Card Design

I need a business card for my company i am starting. I will be providing stump grinding services. I use a motorized machine to grind stumps down under the ground so that they are out of the way and out of sight. I'm looking for my card to have maroon or dark red somewhere in the card to match my truck. I'm going to use this card to advertise and also serve as a design to wrap my truck tailgate as advertisement so i want it to match. the dark maroon color of my truck. I wouldn't mind using bright colors or color for the rest of the card or the lettering or any designs on the card. In the images i have provided i like how there are saw blades integrated into these people advertisements. I also like the illustration of the stump grinder. I also provided a picture of the actual cutting wheel or blade of the grinder.

Industry/Entity Type

Business

Contact Information for Business Card

Company Name - Top Notch Stump Grinding
Phone - 407-218-3952
Email - norris.stumpgrindin@fernmail.com
Name and title - Gerald Norris - Owner and operator
Company Slogan - You find them, I'll grind them

```html
<!DOCTYPE html>
<html lang="en">
<head>
<meta charset="utf-8">
<title>Top Notch Stump Grinding – Business Card</title>
<link rel="stylesheet" href="https://fonts.googleapis.com/css2?family=Raleway:wght@400;500;600;700&display=swap">
<style>
  :root {
    --maroon: #7f1418;
    --maroon-soft: #a3383b;
    --maroon-deep: #5a1213;
    --maroon-dark: #44100f;
    --paper: #ffffff;
  }
  * { margin: 0; padding: 0; box-sizing: border-box; }
  html, body {
    width: 1200px;
    height: 703px;
    overflow: hidden;
    background: var(--paper);
  }
  .card {
    position: relative;
    width: 1200px;
    height: 703px;
    overflow: hidden;
    background: var(--paper);
    font-family: "Raleway", Arial, sans-serif;
    color: var(--maroon);
  }
  .divider-line {
    position: absolute;
    inset: 0;
    width: 1200px;
    height: 703px;
  }
  .grinder-art {
    position: absolute;
    left: 850px;
    top: 0;
    width: 350px;
    height: 505px;
    background: linear-gradient(160deg, var(--maroon) 0%, var(--maroon-soft) 100%);
  }
  .company-name {
    position: absolute;
    left: 57px;
    top: 48px;
    font-size: 38px;
    font-weight: 700;
    white-space: nowrap;
  }
  .slogan {
    position: absolute;
    left: 57px;
    top: 106px;
    font-size: 27px;
    font-weight: 500;
    color: var(--maroon-deep);
    white-space: nowrap;
  }
  .person-name {
    position: absolute;
    left: 54px;
    top: 266px;
    font-size: 90px;
    font-weight: 700;
    line-height: 1;
    white-space: nowrap;
  }
  .name-rule {
    position: absolute;
    left: 57px;
    top: 366px;
    width: 389px;
    height: 4px;
    background: var(--maroon-deep);
  }
  .job-title {
    position: absolute;
    left: 57px;
    top: 378px;
    font-size: 46px;
    font-weight: 400;
    white-space: nowrap;
  }
  .contact {
    position: absolute;
    left: 57px;
    display: flex;
    align-items: center;
    gap: 24px;
    font-size: 31px;
    font-weight: 500;
    white-space: nowrap;
  }
  .contact-phone { top: 560px; }
  .contact-email { top: 608px; }
  .contact-icon {
    width: 40px;
    height: 34px;
    fill: var(--maroon-dark);
    flex: none;
  }
</style>
</head>
<body>
<main class="card">
  <div class="grinder-art" role="img" aria-label="Illustration of a stump grinder cutting wheel with flying wood chips"></div>

  <svg class="divider-line" viewBox="0 0 1200 703" aria-hidden="true">
    <line x1="544" y1="-4" x2="956" y2="707" stroke="var(--maroon-deep)" stroke-width="7"/>
  </svg>

  <h1 class="company-name">Top Notch Stump Grinding</h1>
  <p class="slogan">You find them, I’ll grind them!</p>

  <h2 class="person-name">Gerald Norris</h2>
  <div class="name-rule"></div>
  <p class="job-title">Owner &amp; Operator</p>

  <p class="contact contact-phone">
    <svg class="contact-icon" viewBox="0 0 40 34" aria-hidden="true">
      <path d="M2 10c0-5 8-8 18-8s18 3 18 8v3h-9v-3c-3-1-15-1-18 0v3H2z"/>
      <path d="M9 14h22l6 16v3H3v-3z"/>
      <circle cx="20" cy="23" r="6" fill="var(--paper)"/>
      <circle cx="20" cy="23" r="3"/>
    </svg>
    407-218-3952
  </p>
  <p class="contact contact-email">
    <svg class="contact-icon" viewBox="0 0 40 34" aria-hidden="true">
      <path d="M2 5h36v24H2z"/>
      <path d="M4 7l16 13L36 7" fill="none" stroke="var(--paper)" stroke-width="2"/>
      <path d="M4 27l12-10M36 27L24 17" fill="none" stroke="var(--paper)" stroke-width="2"/>
    </svg>
    norris.stumpgrindin@fernmail.com
  </p>
</main>
</body>
</html>
```